Brevik Fabrication - Business Card Design

We would like a dark (likely black) themed business card to be able to hand out to potential clients. We may list our services on the card or keep it clean. Unsure. Logo attached

```html
<!DOCTYPE html>
<html lang="en">
<head>
<meta charset="utf-8">
<title>Brevik Fabrication – Business Card</title>
<link rel="stylesheet" href="https://fonts.googleapis.com/css2?family=Work+Sans:wght@400;500;800&display=swap">
<style>
  :root {
    --stage: #1b1b1c;
    --card: #222223;
    --card-edge: #2b2b2c;
    --blue: #2a7bd0;
    --orange: #f0622a;
    --ink: #f2f2f2;
  }
  * { margin: 0; padding: 0; box-sizing: border-box; }
  html, body { width: 1200px; height: 900px; overflow: hidden; }
  body {
    background: var(--stage);
    font-family: "Work Sans", Arial, sans-serif;
    color: var(--ink);
    position: relative;
  }
  .card {
    position: absolute;
    left: 250px;
    width: 700px;
    height: 400px;
    background: linear-gradient(135deg, var(--card) 0%, var(--card-edge) 100%);
    border-bottom: 5px solid var(--blue);
  }
  .card--front { top: 40px; }
  .card--back { top: 460px; }

  .brand {
    display: flex;
    flex-direction: column;
    align-items: center;
  }
  .brand__dot {
    width: 64px; height: 64px;
    border-radius: 50%;
    background: var(--orange);
    margin-bottom: 18px;
  }
  .brand__name {
    font-weight: 800;
    color: var(--blue);
    text-transform: uppercase;
    text-align: center;
    line-height: 1.05;
  }
  .card--front .brand {
    position: absolute;
    left: 0; right: 0; top: 110px;
  }
  .card--front .brand__name { font-size: 40px; letter-spacing: 1px; }

  .card--back .brand {
    position: absolute;
    left: 40px; width: 330px; top: 120px;
  }
  .card--back .brand__name { font-size: 34px; }

  .divider {
    position: absolute;
    left: 400px; top: 90px;
    width: 2px; height: 200px;
    background: var(--blue);
  }
  .contact {
    position: absolute;
    left: 430px; top: 90px;
    font-size: 19px;
    line-height: 1.3;
  }
  .contact__name {
    color: var(--blue);
    font-weight: 500;
    font-size: 26px;
    text-transform: uppercase;
    letter-spacing: 0.5px;
  }
  .contact__role { font-size: 20px; margin-bottom: 14px; }
  .contact__address { margin-bottom: 10px; }
  .contact__line { display: flex; align-items: center; gap: 10px; }
  .contact__line svg { width: 14px; height: 14px; flex: none; }
</style>
</head>
<body>
  <section class="card card--front">
    <div class="brand">
      <span class="brand__dot"></span>
      <span class="brand__name">Brevik Fabrication Inc</span>
    </div>
  </section>

  <section class="card card--back">
    <div class="brand">
      <span class="brand__dot"></span>
      <span class="brand__name">Brevik Fabrication Inc</span>
    </div>
    <div class="divider"></div>
    <div class="contact">
      <p class="contact__name">Daniel Hartley</p>
      <p class="contact__role">Founder</p>
      <p class="contact__address">418 Corvin Street<br>Lakeport, WI 53110</p>
      <p class="contact__line">
        <svg viewBox="0 0 16 16" fill="none" stroke="#2a7bd0" stroke-width="1.6"><path d="M4 1.5l2.5 3-1.5 1.5a8 8 0 0 0 5 5l1.5-1.5 3 2.5-1.5 2.5C7 14 2 9 1.5 3z"/></svg>
        (555) 214-7390
      </p>
      <p class="contact__line">
        <svg viewBox="0 0 16 16" fill="none" stroke="#2a7bd0" stroke-width="1.4"><rect x="1.5" y="3.5" width="13" height="9"/><path d="M1.5 3.5l6.5 5 6.5-5"/></svg>
        info@brevikfab.com
      </p>
      <p class="contact__line">
        <svg viewBox="0 0 16 16" fill="none" stroke="#2a7bd0" stroke-width="1.2"><circle cx="8" cy="8" r="6.5"/><ellipse cx="8" cy="8" rx="3" ry="6.5"/><path d="M1.5 8h13M2.5 4.8h11M2.5 11.2h11"/></svg>
        www.brevikfab.com
      </p>
    </div>
  </section>
</body>
</html>
```